Non-profit wants to save the world needs Wordpress presence

My name is Marco Estelani. I'm a photographer who started a charity (Rancho las Brisas) to help the rural schools and health clinics in Central America. We distribute schools supplies and help health clinics with much needed medical supplies and equipment. I need a way to accept donations. I need to have several different writers post to the blog (in Spanish and English). I have a domain name registered (www.rancholasbrisas.org) and started a simple wordpress site as well at http://www.rancholasbrisas.wordpress.com

Industry/Entity Type

Charity

```html
<!DOCTYPE html>
<html lang="en">
<head>
<meta charset="utf-8">
<title>Rancho las Brisas</title>
<link href="https://fonts.googleapis.com/css2?family=Open+Sans:wght@300;400;600;700&display=swap" rel="stylesheet">
<style>
:root{
  --green:#5aa51e;
  --green-dark:#2f7a12;
  --red:#e3151b;
  --red-dark:#b80d12;
  --orange:#f39a0b;
  --yellow:#fcc41a;
  --blue:#1c5fb3;
  --ink:#111;
  --text:#444;
  --muted:#777;
  --paper:#efefec;
  --dark:#1c1c1c;
  --white:#fff;
}
*{box-sizing:border-box;margin:0;padding:0}
html,body{width:1054px;height:1200px;overflow:hidden}
body{position:relative;background:var(--paper);font-family:"Open Sans",Arial,sans-serif;color:var(--text)}
.abs{position:absolute}
.header{left:0;top:0;width:1054px;height:112px;background:var(--white)}
.brand{left:178px;top:10px;display:flex;align-items:center;gap:8px}
.brand-dot{width:34px;height:34px;border-radius:50%;background:var(--green)}
.brand-name{font-weight:700;font-size:18px;color:var(--green-dark)}
.topbar{left:503px;top:0;width:376px;height:36px;background:linear-gradient(#3d9a1c,#247010);border-radius:0 0 3px 3px;display:flex;align-items:center;padding:0 12px;gap:8px;font-size:9px;font-weight:700;color:var(--white)}
.mail{width:13px;height:9px}
.social-box{width:12px;height:12px;border-radius:2px;background:#2aa7e0}
.social-box.alt{background:#3b5998}
.btn-donate-top{background:var(--red);border:1px solid #fff;padding:2px 8px;font-weight:400;font-size:9px}
.ship{margin-left:auto;display:flex;align-items:center;gap:4px}
.flag{width:16px;height:10px;background:#2a3e8c;border:1px solid #fff}
.nav{top:61px;left:0;width:1054px;height:14px;font-size:10.5px;font-weight:300;color:#8a8a8a}
.nav a{position:absolute;text-decoration:none;color:inherit;white-space:nowrap}
.nav a.active{color:#333}
.rule{left:0;width:1054px;height:3px;background:var(--green)}
.hero{left:0;top:115px;width:1054px;height:372px;background:linear-gradient(160deg,#3f5a2a 0%,#6b7a4c 40%,#8a7a5c 65%,#4c5a36 100%)}
.caption{left:175px;top:385px;width:310px;height:100px;background:rgba(20,20,20,.72);color:var(--white);text-align:right;padding:8px 10px}
.caption h2{font-size:15.5px;font-weight:700;line-height:18px;text-transform:uppercase}
.caption p{font-size:10.5px;line-height:14px;margin-top:3px;color:#ddd}
.strip{left:0;top:487px;width:1054px;height:74px;background:linear-gradient(#2a2a2a,#111)}
.thumb{top:498px;width:75px;height:51px;border:1px solid #555}
.t1{background:linear-gradient(#5a6e44,#8c7c5e)}
.t2{background:linear-gradient(90deg,#8a6a3a,#2e7a3e)}
.t3{background:linear-gradient(#6aa68a,#c9a884)}
.arrow{top:516px;width:12px;height:16px}
.tab{top:577px;width:152px;height:71px;background:#fafafa;border:1px solid #ddd;overflow:hidden}
.tab h3{height:29px;line-height:29px;text-align:center;font-weight:300;font-size:16px;color:var(--white)}
.tab p{font-size:8.2px;line-height:10.5px;text-align:center;padding:5px 6px;color:var(--text)}
.tab.mission h3{background:linear-gradient(#fbb234,#e57f07)}
.tab.medical h3{background:linear-gradient(#3c86d6,#1a4f9e)}
.tab.projects h3{background:linear-gradient(#ea3a2a,#b80d12)}
.raise{left:697px;top:577px;width:182px;height:170px;background:linear-gradient(#f5a912,#fcd22a);border:1px solid #e39a0d}
.raise h4{text-align:center;color:var(--white);font-size:13.5px;font-weight:700;margin-top:7px}
.counter{position:absolute;left:24px;top:29px;display:flex;gap:2px}
.counter span{width:15px;height:22px;background:var(--white);border:1px solid #bbb;font-size:12px;font-weight:700;color:#222;text-align:center;line-height:20px}
.progress{position:absolute;left:11px;top:59px;width:162px;height:11px;background:var(--white);border-radius:6px;overflow:hidden;border:1px solid #e3a212}
.progress i{display:block;width:38%;height:100%;background:linear-gradient(#fde36a,#f3b619)}
.amounts{position:absolute;left:25px;top:80px;display:grid;grid-template-columns:repeat(3,38px);gap:6px 11px}
.amounts span{height:18px;background:linear-gradient(#f7a21b,#dc7300);color:var(--white);font-size:9px;text-align:center;line-height:18px;border:1px solid #fff3}
.donate-now{position:absolute;left:35px;top:131px;width:111px;height:23px;background:linear-gradient(#ef2a22,#c70d10);color:var(--white);font-size:13px;text-align:center;line-height:23px;border:1px solid #fff}
.section-title{color:var(--red);font-weight:700;font-size:19.5px;letter-spacing:.3px}
.feature{left:175px;width:245px}
.feature h5{font-size:11px;line-height:14px;color:var(--ink);font-weight:400}
.feature h5 b{font-weight:700}
.feature p{font-size:8.2px;line-height:12.5px;color:var(--muted);margin-top:3px}
.photo{left:441px;width:235px;height:112px}
.ph1{background:linear-gradient(90deg,#a77d45 0%,#8e6a3c 45%,#1f8a4a 60%,#1a6a38 100%)}
.ph2{background:linear-gradient(90deg,#c7b08a,#7fa697 45%,#c08a70)}
.btn-dark{width:84px;height:25px;background:linear-gradient(#3a3a3a,#0c0c0c);color:var(--white);font-size:10.5px;text-align:center;line-height:25px;left:332px}
.latest-sub{left:697px;top:786px;font-size:8.6px;color:#333}
.email{left:697px;top:805px;width:130px;height:18px;background:var(--white);border:1px solid #ccc;font-size:8px;color:#aaa;padding:3px 5px}
.go{left:838px;top:805px;width:41px;height:18px;background:#111;color:var(--white);font-size:10px;text-align:center;line-height:18px}
.blog{left:697px;top:854px;width:182px;height:272px;border:1px solid #ccc;background:var(--white)}
.blog h4{height:31px;background:linear-gradient(#e3151b,#b80d12);color:var(--white);font-size:16px;font-weight:700;padding:4px 8px}
.post{display:flex;height:72px;border-bottom:1px solid #eee}
.post .date{width:45px;background:#e8e8e8;font-size:10px;font-weight:700;color:#333;padding-top:24px;padding-left:5px}
.post .date.hot{color:var(--red)}
.post .body{flex:1;background:#d6d6d6;padding:4px 8px 0 6px}
.post h6{font-size:9px;line-height:11px;font-weight:700;color:#111}
.post p{font-size:7.8px;line-height:10px;color:#555}
.post a{color:#2a5fb0;font-size:7.8px;float:right}
.view-all{position:absolute;left:0;bottom:0;width:180px;height:25px;background:linear-gradient(#3a3a3a,#0a0a0a);color:var(--white);font-size:13.5px;text-align:center;line-height:25px}
.card{top:955px;width:158px;text-align:center}
.card .shot{height:83px;border:2px solid #7cc242}
.card h5{color:var(--red);font-size:10px;font-weight:600;margin-top:9px}
.card p{font-size:8.2px;line-height:11px;color:var(--text);margin-top:3px;text-align:center;padding:0 2px}
.card .more{display:inline-block;margin-top:8px;width:68px;height:23px;background:linear-gradient(#ef2a22,#c70d10);color:var(--white);font-size:8.6px;font-weight:600;line-height:23px}
.footer{left:0;top:1144px;width:1054px;height:56px;background:#1b1b1b;color:var(--white);text-align:center;font-size:8.6px}
.footer nav{margin-top:11px;color:#ddd}
.footer strong{display:block;margin-top:6px;font-size:8px}
</style>
</head>
<body>

<header class="abs header">
  <div class="abs brand"><span class="brand-dot"></span><span class="brand-name">Rancho las Brisas</span></div>
  <div class="abs topbar">
    <svg class="mail" viewBox="0 0 13 9"><rect width="13" height="9" fill="#fff"/><path d="M0 0l6.5 5L13 0" stroke="#2f7a12" fill="none"/></svg>
    <span>Social</span>
    <span class="social-box"></span><span class="social-box alt"></span>
    <span class="btn-donate-top">DONATE</span>
    <span class="ship">Ship to <span class="flag"></span> / USD / Select language</span>
  </div>
  <nav class="abs nav">
    <a class="active" style="left:408px">HOME</a>
    <a style="left:472px">ABOUT US</a>
    <a style="left:553px">MISSION</a>
    <a style="left:627px">SPECIAL PROJECTS</a>
    <a style="left:742px">INFRASTRUCTURE</a>
    <a style="left:854px">BLOG</a>
  </nav>
</header>
<div class="abs rule" style="top:112px"></div>

<section class="abs hero" role="img" aria-label="Photo of volunteers walking a rural dirt path while a photographer kneels in the foreground"></section>
<div class="abs caption">
  <h2>Dr. Lena Park &amp; Nora Velez<br>volunteering at a dental clinic.</h2>
  <p>Dr. Lena Park and Nora Velez volunteering at the Pinecrest Aid Dental Clinic hosted at Riverside Community Hall, Greenfield, OH on May 17, 2014.</p>
</div>

<div class="abs strip"></div>
<svg class="abs arrow" style="left:175px" viewBox="0 0 12 16"><path d="M12 0v16L0 8z" fill="#f39a0b"/></svg>
<div class="abs thumb t1" style="left:204px" role="img" aria-label="Thumbnail: photographer on a village path"></div>
<div class="abs thumb t2" style="left:299px" role="img" aria-label="Thumbnail: man beside a green tarp"></div>
<div class="abs thumb t3" style="left:394px" role="img" aria-label="Thumbnail: children by a wall"></div>
<div class="abs thumb t1" style="left:489px" role="img" aria-label="Thumbnail: photographer on a village path"></div>
<div class="abs thumb t2" style="left:584px" role="img" aria-label="Thumbnail: man beside a green tarp"></div>
<div class="abs thumb t3" style="left:679px" role="img" aria-label="Thumbnail: children by a wall"></div>
<div class="abs thumb t1" style="left:773px" role="img" aria-label="Thumbnail: photographer on a village path"></div>
<svg class="abs arrow" style="left:866px" viewBox="0 0 12 16"><path d="M0 0v16L12 8z" fill="#f39a0b"/></svg>
<div class="abs rule" style="top:561px"></div>

<div class="abs tab mission" style="left:175px"><h3>MISSION</h3><p>This area is dedicated to provide information about medical and dental mission hosted by Pinecrest.</p></div>
<div class="abs tab medical" style="left:349px"><h3>MEDICAL HELP</h3><p>This area is dedicated to provide information about infrastructure programs supported and. . .</p></div>
<div class="abs tab projects" style="left:524px"><h3>SPECIAL PROJECTS</h3><p>This area is used to showcase specific short term projects which might come up</p></div>

<aside class="abs raise">
  <h4>YOU'VE HELPED RAISE...</h4>
  <div class="counter"><span>$</span><span>0</span><span>0</span><span>1</span><span>5</span><span>5</span><span>3</span><span>1</span></div>
  <div class="progress"><i></i></div>
  <div class="amounts"><span>$ 1</span><span>$ 5</span><span>$ 10</span><span>$ 20</span><span>$ 50</span><span>Other</span></div>
  <div class="donate-now">DONATE NOW</div>
</aside>

<h2 class="abs section-title" style="left:175px;top:656px">FEATURE NEWS</h2>
<article class="abs feature" style="top:693px">
  <h5><b>Photographer. Marco Estelani</b> lorem ipsum dolor sit amet, consectetur adipiscing elit.</h5>
  <p>My name is Marco Estelani. I'm a photographer who started a charity (Rancho las Brisas) to help the rural schools and health clinics in Central America.</p>
</article>
<div class="abs photo ph1" style="top:680px" role="img" aria-label="Photo of a man standing in a wooden classroom beside a green tarp"></div>
<div class="abs btn-dark" style="top:767px">READ MORE</div>

<article class="abs feature" style="top:828px">
  <h5><b>Photographer. Marco Estelani</b> lorem ipsum dolor sit amet, consectetur adipiscing elit.</h5>
  <p>My name is Marco Estelani. I'm a photographer who started a charity (Rancho las Brisas) to help the rural schools and health clinics in Central America.</p>
</article>
<div class="abs photo ph2" style="top:814px" role="img" aria-label="Photo of two young girls by a brick wall"></div>
<div class="abs btn-dark" style="top:901px">READ MORE</div>

<h2 class="abs section-title" style="left:697px;top:760px">LATEST NEWS</h2>
<p class="abs latest-sub">Events, stories, giveaways and upcoming events</p>
<div class="abs email">Email</div>
<div class="abs go">&gt;&gt; GO</div>

<aside class="abs blog">
  <h4>BLOG</h4>
  <div class="post"><div class="date hot">Sep-19</div><div class="body"><h6>LOREM IPSUM DOLOR SIT AM ET, CONSECTE</h6><p>Adipiscing elit. Etiam sed sodales neque. Nulla vel risus vitae orci pharetra rhoncu <a>Read more</a></p></div></div>
  <div class="post"><div class="date">Sep-18</div><div class="body"><h6>LOREM IPSUM DOLOR SIT AM ET, CONSECTE</h6><p>Adipiscing elit. Etiam sed sodales neque. Nulla vel risus vitae orci pharetra rhoncu <a>Read more</a></p></div></div>
  <div class="post"><div class="date">Sep-17</div><div class="body"><h6>LOREM IPSUM DOLOR SIT AM ET, CONSECTE</h6><p>Adipiscing elit. Etiam sed sodales neque. Nulla vel risus vitae orci pharetra rhoncu <a>Read more</a></p></div></div>
  <div class="view-all">VIEW ALL</div>
</aside>

<article class="abs card" style="left:175px">
  <div class="shot ph1" role="img" aria-label="Photo of a man in a wooden classroom"></div>
  <h5>ETIAM SUSCIPIT FEUGIAT</h5>
  <p>Lorem ipsum dolor sit amet, consectetur adipiscing elit. Maecenas tristique turpis nec orci bibendum, a luctus risus</p>
  <span class="more">› More Details</span>
</article>
<article class="abs card" style="left:347px">
  <div class="shot ph2" role="img" aria-label="Photo of two girls by a wall"></div>
  <h5>ETIAM SUSCIPIT FEUGIAT</h5>
  <p>Lorem ipsum dolor sit amet, consectetur adipiscing elit. Maecenas tristique turpis nec orci bibendum, a luctus risus</p>
  <span class="more">› More Details</span>
</article>
<article class="abs card" style="left:520px">
  <div class="shot t1" role="img" aria-label="Photo of a photographer on a village path"></div>
  <h5>ETIAM SUSCIPIT FEUGIAT</h5>
  <p>Lorem ipsum dolor sit amet, consectetur adipiscing elit. Maecenas tristique turpis nec orci bibendum, a luctus risus</p>
  <span class="more">› More Details</span>
</article>

<footer class="abs footer">
  <nav>HOME &nbsp;|&nbsp; ABOUT US &nbsp;|&nbsp; MISSION &nbsp;|&nbsp; SPECIAL PROJECTS &nbsp;|&nbsp; INFRASTRUCTURE &nbsp;|&nbsp; BLOG</nav>
  <strong>ALL RIGHTS RESERVED</strong>
</footer>

</body>
</html>
```